Business Card Design Project

I want a cleaner business card and envelope then what we have now, its too crowded.
Updates

I update with logo, this can be changed anyway you feel it looks best. I also have put gaurantee on there and extended time, this is my first time doing this. Also gave an example of current card

Target Market(s)

a wide array of customers from lattice 700 to small companies and cleints

Industry/Entity Type

Business

Requirements
Must have
• Need to have address, telephone number email
Nice to have
• a sharp professional card that stands out but is still very clean.
Should not have
• Not crazy looking

```html
<!DOCTYPE html>
<html lang="en">
<head>
<meta charset="utf-8">
<title>Marlow Insurance Group — Business Card</title>
<link href="https://fonts.googleapis.com/css2?family=Source+Sans+3:wght@400;600&display=swap" rel="stylesheet">
<style>
  :root {
    --backdrop: #1c1c1c;
    --card-stock: #e9e5d6;
    --ink-dark: #1f1f1f;
    --ink-soft: #5a5a55;
    --rule: #6f6d66;
    --mark-grey: #9c9c9c;
  }
  * { margin: 0; padding: 0; box-sizing: border-box; }
  html, body {
    width: 1200px; height: 907px; overflow: hidden;
    background: var(--backdrop);
    font-family: "Source Sans 3", Arial, sans-serif;
  }
  .stage { position: relative; width: 1200px; height: 907px; }
  .card {
    position: absolute;
    width: 520px; height: 298px;
    background: var(--card-stock);
    box-shadow: 0 8px 24px rgba(0,0,0,.5);
  }
  .card--front { left: 50px; top: 304px; }
  .card--back { left: 630px; top: 304px; }

  .brand { display: flex; align-items: center; gap: 12px; }
  .brand__square { width: 44px; height: 44px; background: var(--mark-grey); flex: none; }
  .brand__name {
    font-weight: 600; color: var(--ink-dark);
    text-transform: uppercase; letter-spacing: .08em; line-height: 1.05;
  }
  .card--front .brand { position: absolute; left: 56px; top: 44px; }
  .card--front .brand__name { font-size: 21px; }
  .brand__name small { display: block; font-size: .55em; letter-spacing: .2em; }

  .holder { position: absolute; left: 72px; top: 136px; color: var(--ink-soft); }
  .holder__name { font-size: 19px; }
  .holder__title { font-size: 17px; margin-top: 2px; }

  .divider { position: absolute; left: 266px; top: 118px; width: 1px; height: 146px; background: var(--rule); }
  .contact { position: absolute; left: 282px; top: 118px; color: var(--ink-soft); font-size: 12.5px; line-height: 18px; }
  .contact__group + .contact__group { margin-top: 20px; }

  .card--back .brand {
    position: absolute; left: 0; right: 0; top: 0; bottom: 0;
    flex-direction: column; justify-content: center; gap: 16px;
  }
  .card--back .brand__square { width: 64px; height: 64px; }
  .card--back .brand__name { font-size: 30px; text-align: center; }
</style>
</head>
<body>
<main class="stage">
  <section class="card card--front" aria-label="Card front">
    <div class="brand">
      <span class="brand__square"></span>
      <span class="brand__name">Marlow<small>Insurance Group</small></span>
    </div>
    <div class="holder">
      <p class="holder__name">Paula Wren-Hastings</p>
      <p class="holder__title">Operations Manager</p>
    </div>
    <span class="divider"></span>
    <address class="contact" style="font-style:normal">
      <div class="contact__group">
        <p>Phone: 555-210-4400 ext 118</p>
        <p>Direct: 555-210-4471</p>
        <p>Fax: 555-210-4403</p>
        <p>pwren-hastings@marlowagency.com</p>
      </div>
      <div class="contact__group">
        <p>1870 Orchard Lane</p>
        <p>Fairview, MI 48000</p>
        <p>www.marlowagency.com</p>
      </div>
    </address>
  </section>

  <section class="card card--back" aria-label="Card back">
    <div class="brand">
      <span class="brand__square"></span>
      <span class="brand__name">Marlow<small>Insurance Group</small></span>
    </div>
  </section>
</main>
</body>
</html>
```